Brimvale Website

I need a design of homepage for a health and wellness center. We considers self to be young and fresh and want something along that design. We want a main picture/logo/design (or all three), and underneath that 4 pictures to depict what services we do. The four services are Orthopedic Rehab, Neurological Rehab, Speech Pathology and Float. I have attached our logo, and some pictures that might be helpful, but the pictures don't have to be included. Here is an example of what I would like it look. http://pixelbazaar.net/web-design/contests/lumotrek-website-design-needed-more-work-come-submit-517306/entries/84126759

```html
<!DOCTYPE html>
<html lang="en">
<head>
<meta charset="utf-8">
<title>Brimvale — Center for Health &amp; Recovery</title>
<link href="https://fonts.googleapis.com/css2?family=Open+Sans:wght@300;400;600&display=swap" rel="stylesheet">
<style>
:root{
  --navy:#33475c;
  --navy-deep:#2c3d50;
  --hex:#2f4259;
  --blue:#3498db;
  --teal:#1abc9c;
  --text:#4a5561;
  --muted:#707a84;
  --light-band:#f4f4f4;
  --white:#ffffff;
  --field:#4e6278;
}
*{margin:0;padding:0;box-sizing:border-box}
html,body{width:1200px;height:3120px;overflow:hidden}
body{font-family:"Open Sans",Arial,sans-serif;color:var(--text);background:var(--white);position:relative}
.abs{position:absolute}

/* hero */
.hero{left:0;top:0;width:1200px;height:700px;background:linear-gradient(160deg,#7f8fa1 0%,#5d6f84 40%,#3c5068 100%)}
.hero-wave{left:0;top:560px;width:1200px;height:160px}
.brand{left:229px;top:64px;display:flex;align-items:center;gap:10px;color:#e9eef3;font-size:26px;font-weight:400}
.brand-dot{width:26px;height:26px;border-radius:50%;background:#8fc44a}
.nav{left:568px;top:68px;display:flex;gap:22px;font-size:15px;color:var(--white)}
.nav a{color:var(--white);text-decoration:none;position:relative}
.nav a.active::after{content:"";position:absolute;left:-4px;right:-4px;top:28px;height:3px;background:var(--blue)}
.tablet{left:229px;top:258px;width:329px;height:428px;background:#f4f4f4;border-radius:14px;box-shadow:0 6px 18px rgba(0,0,0,.15)}
.tablet-cam{left:161px;top:17px;width:5px;height:5px;border-radius:50%;background:#555}
.tablet-screen{left:33px;top:35px;width:262px;height:356px;background:linear-gradient(170deg,#6d8f3c,#a3b54f 55%,#5e7a2d)}
.hero-title{left:589px;top:298px;font-size:27px;color:var(--white);font-weight:400}
.hero-copy{left:589px;top:358px;width:395px;font-size:14px;line-height:24px;color:#e2e8ee}
.btn{display:flex;align-items:center;justify-content:center;color:var(--white);font-size:15px;border-radius:2px}
.hero-btn{left:738px;top:476px;width:138px;height:44px;background:var(--blue)}

/* about */
.section-title{font-size:21px;color:var(--navy);font-weight:400}
.about-title{left:229px;top:786px}
.about-copy{left:229px;top:825px;width:480px;font-size:14px;line-height:23px;color:var(--text)}
.about-photo{left:734px;top:832px;width:246px;height:144px;background:linear-gradient(180deg,#8fb4d6,#a8c9e4 55%,#6a9a45)}

/* services */
.services{left:0;top:1034px;width:1200px;height:302px;background:var(--light-band)}
.service{width:240px;text-align:center;top:1071px}
.service-photo{width:110px;height:68px;margin:0 auto}
.service-name{margin-top:38px;font-size:15px;color:#222}
.service-copy{margin-top:12px;font-size:11px;line-height:15px;color:var(--muted)}

/* slider */
.slider{left:0;top:1337px;width:1200px;height:407px;background:linear-gradient(180deg,#3e536b 0%,#5b6f86 55%,#7e8ea0 100%)}
.slider-title{left:0;top:1378px;width:1200px;text-align:center;font-size:25px;color:var(--white)}
.slider-sub{left:0;top:1414px;width:1200px;text-align:center;font-size:14px;color:#dde4eb}
.arrow{top:1545px;width:40px;height:70px}
.laptop-lid{left:414px;top:1508px;width:389px;height:258px;background:#2a2a2a;border-radius:10px 10px 0 0}
.laptop-screen{left:11px;top:19px;width:367px;height:228px;background:linear-gradient(180deg,#4f7f3a,#78a24e 50%,#3c5f2c)}
.laptop-base{left:364px;top:1764px;width:489px;height:28px;background:linear-gradient(180deg,#f2f2f2,#cfcfcf);border-radius:0 0 20px 20px;box-shadow:0 14px 20px rgba(0,0,0,.12)}
.laptop-notch{left:211px;top:0;width:66px;height:6px;background:#b5b5b5;border-radius:0 0 6px 6px}

/* testimonials */
.people-title{left:0;top:1892px;width:1200px;text-align:center;font-size:40px;font-weight:300;color:var(--navy)}
.quote{width:370px;height:140px}
.quote svg{position:absolute;left:0;top:0}
.quote-name{position:absolute;left:131px;top:20px;font-size:19px;color:var(--navy)}
.quote-copy{position:absolute;left:131px;top:62px;width:235px;font-size:11px;line-height:15px;color:var(--muted)}

/* contact */
.contact{left:0;top:2538px;width:1200px;height:453px;background:var(--navy)}
.contact-title{left:229px;top:2618px;font-size:21px;color:var(--white)}
.contact-copy{left:229px;top:2660px;width:335px;font-size:11px;line-height:16px;color:#aab6c3}
.contact-line{left:229px;display:flex;align-items:center;gap:9px;font-size:11px;color:#dbe2e9}
.field{background:var(--field);font-size:11px;color:#b7c2cd;padding:8px 10px;border-radius:2px}
.select-tab{right:0;top:0;width:30px;height:31px;background:var(--teal)}
.reset{left:693px;top:2854px;width:131px;height:44px;background:var(--teal)}
.submit{left:842px;top:2854px;width:136px;height:44px;background:var(--blue)}
.footer{left:0;top:2991px;width:1200px;height:129px;background:var(--navy-deep)}
.footer-notch{left:586px;top:2977px;width:28px;height:14px}
.copyright{left:0;top:3050px;width:1200px;text-align:center;font-size:11px;color:#e3e8ee}
</style>
</head>
<body>

<header>
  <div class="abs hero"></div>
  <svg class="abs hero-wave" viewBox="0 0 1200 160" preserveAspectRatio="none" aria-hidden="true">
    <path d="M0 130 C240 120 420 70 640 62 C860 55 1040 95 1200 140 L1200 160 L0 160 Z" fill="#ffffff"/>
  </svg>
  <div class="abs brand"><span class="brand-dot"></span>Brimvale</div>
  <nav class="abs nav">
    <a class="active">Home</a><a>About</a><a>Service</a><a>Features</a><a>Price</a><a>Contact</a>
  </nav>
  <div class="abs tablet">
    <div class="abs tablet-cam"></div>
    <div class="abs tablet-screen" role="img" aria-label="Woman stretching her arms outdoors on a sunny lawn"></div>
  </div>
  <h1 class="abs hero-title">Quam eleifend metus commodo</h1>
  <p class="abs hero-copy">luctus at sit amet urna. Quisque non augue tincidunt, egest as massa non, elementum sem. Suspendisse mollis nulla eu lorem ultricies dapibus.</p>
  <a class="abs btn hero-btn">Learn more</a>
</header>

<section>
  <h2 class="abs section-title about-title">About us</h2>
  <p class="abs about-copy">Sed non massa quis nisl tincidunt posuere sit amet vitae sem. Praesent sed convallis quam. Donec hendrerit neque sit amet tellus ornare et semper lorem lacinia. Suspendisse ac pellentesque odio. Nunc pharetra malesuada nisi ac condimentum. Curabitur porttitor pulvinar</p>
  <div class="abs about-photo" role="img" aria-label="Mother and child meditating together on grass"></div>
</section>

<section>
  <div class="abs services"></div>
  <div class="abs service" style="left:238px">
    <div class="service-photo" role="img" aria-label="Therapist treating a patient's leg" style="background:linear-gradient(135deg,#6d5a4c,#b89c86)"></div>
    <div class="service-name">Orthopedic Rehab</div>
    <p class="service-copy">Curabitur tincidunt dapibus odio, eu gravida felis blandit vel. Vivamus feugiat auctor lorem non eleifend. Nam eu pellentesque est, vitae interdum nisi.</p>
  </div>
  <div class="abs service" style="left:485px">
    <div class="service-photo" role="img" aria-label="Colourful brain illustration on dark background" style="background:radial-gradient(circle,#c0392b,#2c5a8a 55%,#0d0d0d)"></div>
    <div class="service-name">Neurological Rehab</div>
    <p class="service-copy">Nullam dignissim felis diam, sed ultricies nisl ultricies quis. Maecenas feugiat urna ante, et viverra tellus facilisis ut. In hac habitasse platea dictumst.</p>
  </div>
  <div class="abs service" style="left:735px">
    <div class="service-photo" role="img" aria-label="Children in a speech therapy session" style="background:linear-gradient(135deg,#4e8a7e,#c7a58a)"></div>
    <div class="service-name">Speech Pathology and Float</div>
    <p class="service-copy">Aliquam mattis massa at urna tincidunt ultrices. Curabitur lobortis ante vulputate, imperdiet felis a, adipiscing odio aliquam pharetra molestie mauris.</p>
  </div>
</section>

<section>
  <div class="abs slider"></div>
  <h2 class="abs slider-title">Lorem ipsum dolor sit amet</h2>
  <p class="abs slider-sub">consectetur adipiscing elit. Maecenas facilisis ligula non ornare vehicula.</p>
  <svg class="abs arrow" style="left:225px" viewBox="0 0 40 70" aria-hidden="true"><path d="M32 4 L8 35 L32 66" fill="none" stroke="#fff" stroke-width="7"/></svg>
  <svg class="abs arrow" style="left:941px" viewBox="0 0 40 70" aria-hidden="true"><path d="M8 4 L32 35 L8 66" fill="none" stroke="#fff" stroke-width="7"/></svg>
  <div class="abs laptop-lid">
    <div class="abs laptop-screen" role="img" aria-label="Woman in white meditating in a green forest"></div>
  </div>
  <div class="abs laptop-base"><div class="abs laptop-notch"></div></div>
</section>

<section>
  <h2 class="abs people-title">What People Say</h2>
  <div class="abs quote" style="left:229px;top:1999px">
    <svg width="116" height="138" viewBox="0 0 116 138" aria-hidden="true"><path d="M58 3 L112 33 Q116 36 116 42 L116 96 Q116 102 112 105 L58 135 L4 105 Q0 102 0 96 L0 42 Q0 36 4 33 Z" fill="#2f4259"/></svg>
    <div class="quote-name">Excepteur sint occaecat</div>
    <p class="quote-copy">Sed non massa quis nisl tincidunt posuere sit amet vitae sem. Praesent sed convallis quam.</p>
  </div>
  <div class="abs quote" style="left:614px;top:1999px">
    <svg width="116" height="138" viewBox="0 0 116 138" aria-hidden="true"><path d="M58 3 L112 33 Q116 36 116 42 L116 96 Q116 102 112 105 L58 135 L4 105 Q0 102 0 96 L0 42 Q0 36 4 33 Z" fill="#2f4259"/></svg>
    <div class="quote-name">Excepteur sint occaecat</div>
    <p class="quote-copy">Sed non massa quis nisl tincidunt posuere sit amet vitae sem. Praesent sed convallis quam.</p>
  </div>
  <div class="abs quote" style="left:229px;top:2152px">
    <svg width="116" height="138" viewBox="0 0 116 138" aria-hidden="true"><path d="M58 3 L112 33 Q116 36 116 42 L116 96 Q116 102 112 105 L58 135 L4 105 Q0 102 0 96 L0 42 Q0 36 4 33 Z" fill="#2f4259"/></svg>
    <div class="quote-name">Excepteur sint occaecat</div>
    <p class="quote-copy">Sed non massa quis nisl tincidunt posuere sit amet vitae sem. Praesent sed convallis quam.</p>
  </div>
  <div class="abs quote" style="left:614px;top:2152px">
    <svg width="116" height="138" viewBox="0 0 116 138" aria-hidden="true"><path d="M58 3 L112 33 Q116 36 116 42 L116 96 Q116 102 112 105 L58 135 L4 105 Q0 102 0 96 L0 42 Q0 36 4 33 Z" fill="#2f4259"/></svg>
    <div class="quote-name">Excepteur sint occaecat</div>
    <p class="quote-copy">Sed non massa quis nisl tincidunt posuere sit amet vitae sem. Praesent sed convallis quam.</p>
  </div>
  <div class="abs quote" style="left:229px;top:2305px">
    <svg width="116" height="138" viewBox="0 0 116 138" aria-hidden="true"><path d="M58 3 L112 33 Q116 36 116 42 L116 96 Q116 102 112 105 L58 135 L4 105 Q0 102 0 96 L0 42 Q0 36 4 33 Z" fill="#2f4259"/></svg>
    <div class="quote-name">Excepteur sint occaecat</div>
    <p class="quote-copy">Sed non massa quis nisl tincidunt posuere sit amet vitae sem. Praesent sed convallis quam.</p>
  </div>
  <div class="abs quote" style="left:614px;top:2305px">
    <svg width="116" height="138" viewBox="0 0 116 138" aria-hidden="true"><path d="M58 3 L112 33 Q116 36 116 42 L116 96 Q116 102 112 105 L58 135 L4 105 Q0 102 0 96 L0 42 Q0 36 4 33 Z" fill="#2f4259"/></svg>
    <div class="quote-name">Excepteur sint occaecat</div>
    <p class="quote-copy">Sed non massa quis nisl tincidunt posuere sit amet vitae sem. Praesent sed convallis quam.</p>
  </div>
</section>

<footer>
  <div class="abs contact"></div>
  <h2 class="abs contact-title">Curabitur ornare neque</h2>
  <p class="abs contact-copy">Id sagittis commodo. Vivamus rhoncus feugiat leo id dictum. Nulla fermentum nibh eu velit molestie ultricies. Curabitur non gravida urna, at varius tortor. Donec feugiat, nisl ultrices adipiscing pharetra, augue lorem pharetra tortor, non tincidunt urna diam in libero. Nam et neque ut nisi consectetur tempor. Maecenas gravida est eu nisl dignissim gravida. Proin mollis sodales ullamcorper.</p>
  <div class="abs contact-line" style="top:2788px">
    <svg width="12" height="16" viewBox="0 0 12 16" aria-hidden="true"><path d="M6 0 A6 6 0 0 1 12 6 C12 10 6 16 6 16 C6 16 0 10 0 6 A6 6 0 0 1 6 0 Z" fill="#fff"/><circle cx="6" cy="6" r="2.2" fill="#33475c"/></svg>
    venenatis neque sit amet ante aliquam sollicitudin</div>
  <div class="abs contact-line" style="top:2817px">
    <svg width="13" height="13" viewBox="0 0 24 24" aria-hidden="true"><path d="M6.6 10.8c1.4 2.8 3.8 5.1 6.6 6.6l2.2-2.2c.3-.3.7-.4 1-.2 1.1.4 2.3.6 3.6.6.6 0 1 .4 1 1V20c0 .6-.4 1-1 1C10.6 21 3 13.4 3 4c0-.6.4-1 1-1h3.5c.6 0 1 .4 1 1 0 1.3.2 2.5.6 3.6.1.3 0 .7-.2 1z" fill="#fff"/></svg>
    0555-0142-21 &nbsp; / &nbsp; 0555-019-222-111</div>
  <div class="abs contact-line" style="top:2845px">
    <svg width="14" height="10" viewBox="0 0 14 10" aria-hidden="true"><rect width="14" height="10" rx="1" fill="#fff"/><path d="M0 1 L7 6 L14 1" fill="none" stroke="#33475c" stroke-width="1.3"/></svg>
    hello@brimvale-mail.org</div>

  <div class="abs field" style="left:612px;top:2627px;width:176px;height:31px">your name</div>
  <div class="abs field" style="left:805px;top:2627px;width:173px;height:31px">your email</div>
  <div class="abs field" style="left:612px;top:2673px;width:366px;height:31px">your subject
    <div class="abs select-tab"><svg width="30" height="31" viewBox="0 0 30 31" aria-hidden="true"><path d="M10 12 L20 12 L15 19 Z" fill="#fff"/></svg></div>
  </div>
  <div class="abs field" style="left:612px;top:2719px;width:366px;height:118px">your message</div>
  <a class="abs btn reset">Reset</a>
  <a class="abs btn submit">Submit</a>

  <div class="abs footer"></div>
  <svg class="abs footer-notch" viewBox="0 0 28 14" aria-hidden="true"><path d="M0 14 L14 0 L28 14 Z" fill="#2c3d50"/></svg>
  <p class="abs copyright">Copyright 2014 Brimvale, All right reserved.</p>
</footer>

</body>
</html>
```